New shirt company looking for a fun and edgy online retail website design

We're a new company looking for a simple yet attractive website to sell shirts/tops to a mostly younger female audience. Our name is Tavi Shirt Co. and the PlanHerd logo is uploaded. We're thinking a home page, three separate pages for our shirt "collections", and a contact page/cart page for a grand total of 5 pages. We'd like the website to be coded, easy for the consumer to navigate/shop/checkout, and easy to link to various social media platforms and online websites. For colors, we're aiming for various blues, light grey, and maybe tan/khaki. Our goal is to launch with approximately 20-30 tops/shirts (or 7-10) per page. Please let us know if you have any questions and thank you for helping us! We are very excited to see what is created!

Target Market(s)

Female teens to early twenties

Coding

Coded - Design and coding required

Number of Pages Required

3 page

Font styles to use
Decorative
Script

Colors
cee9f5
85cae6
33a6d7
0393ce
cfdfed
85acd3

Requirements
Must have
• Online shopping/purchasing capabilities, dropdowns to select sizes for each item, easy to add/remove new or seasoned items.

```html
<!DOCTYPE html>
<html lang="en">
<head>
<meta charset="utf-8">
<title>Tavi Shirt Co. — Home</title>
<link href="https://fonts.googleapis.com/css2?family=Delius&family=Sniglet:wght@400;800&display=swap" rel="stylesheet">
<style>
:root{
  --sky:#cee9f5;
  --blue:#85cae6;
  --accent:#33a6d7;
  --deep:#0393ce;
  --navy:#0b3f8f;
  --grey:#f1f1f1;
  --ink:#2f2f2f;
  --muted:#7a7a7a;
  --white:#ffffff;
  --night:#1a1a1a;
}
*{box-sizing:border-box;margin:0;padding:0}
html,body{width:768px;height:1200px;overflow:hidden}
body{font-family:"Delius",cursive;color:var(--ink);background:var(--sky);position:relative}
.abs{position:absolute}
.topbar{left:0;top:0;width:768px;height:26px;background:var(--grey);border-bottom:1px solid #ddd;font-size:7px;color:var(--muted)}
.topbar span{position:absolute;top:9px}
.header{left:0;top:26px;width:768px;height:46px;background:var(--blue)}
.brand{font-family:"Delius",cursive;color:var(--navy);font-size:13px;display:flex;align-items:center;gap:4px}
.brand i{display:inline-block;width:8px;height:8px;background:var(--navy)}
.search{left:253px;top:10px;width:308px;height:24px;background:var(--sky);border-radius:2px;font-size:7.5px;display:flex;align-items:center}
.search .cat{padding:0 8px;border-right:1px solid var(--ink);height:16px;line-height:16px}
.search .field{flex:1;padding-left:7px;color:#9ab}
.search svg{margin:0 10px}
.cart{left:569px;top:10px;width:84px;height:24px;background:var(--sky);border-radius:2px;font-size:7.5px;display:flex;align-items:center;gap:8px;padding-left:8px}
.nav{left:0;top:72px;width:768px;height:27px;background:var(--grey);border-bottom:1px solid #ddd;font-size:7.5px}
.nav a{position:absolute;top:8px;color:var(--ink);text-decoration:none}
.nav a.active{color:var(--deep);border-bottom:1.5px solid var(--deep);padding-bottom:6px}
.social{display:flex;gap:6px}
.social b{width:13px;height:13px;border-radius:50%;background:var(--deep);display:block}
.hero{left:0;top:99px;width:768px;height:312px;background:linear-gradient(180deg,#fbcfd8,#f1b3c6)}
.hero-photo{left:90px;top:0;width:300px;height:312px;background:radial-gradient(ellipse at 45% 55%,#f3e6e4 0%,#e7bfb7 40%,rgba(241,179,198,0) 72%)}
.hero h1{right:115px;top:84px;font-family:"Sniglet",cursive;font-weight:800;font-size:22px;line-height:29px;text-align:right;color:var(--white)}
.btn-outline{left:593px;top:179px;width:60px;height:24px;border:1.5px solid var(--white);border-radius:2px;color:var(--white);font-size:7px;display:flex;align-items:center;justify-content:center}
.dots{left:371px;top:389px;display:flex;gap:4px}
.dots b{width:6px;height:6px;border-radius:50%;border:1px solid var(--white)}
.dots b.on{background:var(--white)}
.section-title{font-family:"Sniglet",cursive;font-weight:800;font-size:23px;color:var(--ink)}
.tile{width:260px;height:288px;top:479px}
.tile-blue{left:117px;background:linear-gradient(180deg,#0d3569,#0a2c57);display:flex;align-items:center;justify-content:center;color:var(--white);font-size:12px;gap:5px}
.tile-orange{left:393px;background:linear-gradient(180deg,#fba800,#ef8a06)}
.band{left:0;top:778px;width:768px;height:38px;background:var(--blue)}
.band p{position:absolute;left:237px;top:12px;font-size:11.5px}
.btn-soft{left:460px;top:7px;width:71px;height:24px;background:var(--sky);border-radius:2px;font-size:7.5px;display:flex;align-items:center;justify-content:center}
.feature{left:117px;top:862px;width:536px;height:169px;background:linear-gradient(90deg,#c08c5c,#a97a55 40%,#c79a6e 70%,#b27c56)}
.footer{left:0;top:1050px;width:768px;height:134px;background:var(--blue);font-size:7.5px;color:var(--white)}
.footer a{position:absolute;color:var(--white);text-decoration:none}
.footer a.active{color:var(--deep)}
.copy{left:0;top:1184px;width:768px;height:16px;background:var(--night);color:var(--white);font-size:7px;text-align:center;line-height:16px}
</style>
</head>
<body>
<div class="abs topbar">
  <svg class="abs" style="left:117px;top:10px" width="9" height="7" viewBox="0 0 9 7"><rect x=".5" y=".5" width="8" height="6" fill="none" stroke="#888"/><path d="M.5 .5 4.5 4 8.5 .5" fill="none" stroke="#888"/></svg>
  <span style="left:131px">hello@tavishirts.shop</span>
  <svg class="abs" style="left:210px;top:9px" width="8" height="8" viewBox="0 0 8 8"><path d="M1 1c1-1 2 0 2 1L2.4 3c.6 1.2 1.4 2 2.6 2.6l1-.6c1 0 2 1 1 2-3 1-7-3-6-7z" fill="none" stroke="#888" stroke-width=".8"/></svg>
  <span style="left:223px">+(00) 12-3456-7890</span>
  <span style="left:485px">Wishlist ♡</span>
  <span style="left:542px">Checkout ⌄</span>
  <span style="left:603px">My account</span>
</div>

<header class="abs header">
  <div class="abs brand" style="left:117px;top:16px"><i></i>Tavi Shirt Co.</div>
  <div class="abs search">
    <span class="cat">All categories ⌄</span>
    <span class="field">Search here</span>
    <svg width="10" height="10" viewBox="0 0 10 10"><circle cx="4" cy="4" r="3.2" fill="none" stroke="#333"/><path d="M6.4 6.4 9.3 9.3" stroke="#333"/></svg>
  </div>
  <div class="abs cart">
    <svg width="12" height="11" viewBox="0 0 12 11"><circle cx="3" cy="3" r="3" fill="#33a6d7"/><rect x="3" y="4" width="8" height="6" rx="1" fill="none" stroke="#333"/></svg>
    <span>Cart - $29.00</span>
  </div>
</header>

<nav class="abs nav">
  <a class="active" style="left:117px">Home</a>
  <a style="left:168px">Our top picks</a>
  <a style="left:248px">Store</a>
  <a style="left:299px">Buy</a>
  <div class="abs social" style="left:565px;top:7px"><b></b><b></b><b></b><b></b><b></b></div>
</nav>

<section class="abs hero">
  <div class="abs hero-photo" role="img" aria-label="Smiling woman in a white t-shirt pointing toward the headline"></div>
  <h1 class="abs">Get great shirts/tops<br>at an unbelievably<br>reasonable price.</h1>
  <div class="abs btn-outline">Shop now</div>
  <div class="abs dots"><b class="on"></b><b></b><b></b></div>
</section>

<h2 class="abs section-title" style="left:117px;top:431px">Trending</h2>
<div class="abs tile tile-blue" role="img" aria-label="Young woman in a red hoodie with fingers crossed on a navy backdrop">
  <span>Visit store</span>
  <svg width="17" height="8" viewBox="0 0 17 8"><path d="M0 4h16M12 .5 16 4l-4 3.5" fill="none" stroke="#fff" stroke-width="1.2"/></svg>
</div>
<div class="abs tile tile-orange" role="img" aria-label="Girl in a teal lace top looking up thoughtfully on an orange backdrop"></div>

<div class="abs band">
  <p>Have a look at our collections!</p>
  <div class="abs btn-soft">Visit store</div>
</div>

<h2 class="abs section-title" style="left:117px;top:821px">Featured</h2>
<div class="abs feature" role="img" aria-label="Three laughing friends in denim and casual tops on a tan backdrop"></div>

<footer class="abs footer">
  <div class="abs brand" style="left:117px;top:56px;font-size:15px"><i></i>Tavi Shirt Co.</div>
  <a style="left:318px;top:30px">Home</a>
  <a class="active" style="left:318px;top:51px">Our top picks</a>
  <a style="left:318px;top:72px">Store</a>
  <a style="left:318px;top:94px">Buy</a>
  <a style="left:410px;top:30px">Wishlist</a>
  <a style="left:410px;top:51px">Checkout</a>
  <a style="left:410px;top:72px">My account</a>
  <span class="abs" style="right:115px;top:30px">Visit our social media:</span>
  <div class="abs social" style="left:565px;top:47px"><b></b><b></b><b></b><b></b><b></b></div>
</footer>

<div class="abs copy">© copyright 2020 Tavi</div>
</body>
</html>
```